Scrum Master & Agile IT Coach Needing Business Website

Hello, my name is Brent Holloway
I am a project manger, scrum master, & agile coach. I work with IT development teams on major projects for Tier One companies . My project management business has a website and can be found here: www.tq-keystride.example

I have launched a new company, ALL focused on IT Agile Coaching, I am looking to have a website created for my new company - the name of the new company is: Pins and Dials - Agile IT Coaching and Training.
I have a logo and it is provided in the materials. I like to logo; I am open to different color pallets.

The website will have a total of 7 pages; I have content for 5 of the 7 pages prepared; the other 2 pages will say under construction.

Page 1 Who am I, What I do, My Experience
Demonstrated experience and progression from Scrum Master to
Program Manager to Coach

Page 2 Pins & Dials - Agile Team Coaching
teams working major IT projects, multiple months/years

Page 3 Coaching @ the Team Level

Page 4 Coaching @ the Program Level ; LYNQ BQR level

Pages 5 -6 Under Construction

Page 7 Presentations, Slide Decks, Reference Materials

Mentor Nook need to have this highlighted somewhere Monthly Blog
Updates

Industry/Entity Type

IT development

Coding

Coded - Design and coding required

Number of Pages Required

5+ page

Requirements
Must have
• the website must be bold - I want those who visit to remember coming to my coaching site
Nice to have
• nice to have will be a modern / futuristic website; I work with IT developers, I want a website they will like
Should not have
• should not be stiff - it should be professional but fun

```html
<!DOCTYPE html>
<html lang="en">
<head>
<meta charset="utf-8">
<title>Pins &amp; Dials - Agile IT Coaching &amp; Training</title>
<link href="https://fonts.googleapis.com/css2?family=Poppins:wght@300;400;500;600;700;800&family=Courier+Prime:ital@1&display=swap" rel="stylesheet">
<style>
:root{
  --navy:#0b2a5e;
  --navy-deep:#0a2350;
  --blue:#0a8ad6;
  --blue-soft:#2aa3ea;
  --ink:#14213d;
  --text:#4a5468;
  --light:#f2f4f8;
  --white:#ffffff;
  --line:#dfe4ec;
}
*{box-sizing:border-box;margin:0;padding:0}
html,body{width:1200px;height:4769px;overflow:hidden}
body{position:relative;font-family:"Poppins",sans-serif;color:var(--text);background:var(--white)}
.abs{position:absolute}
a{color:var(--navy)}

/* header */
.brand{left:93px;top:20px;display:flex;align-items:center;gap:12px}
.brand-mark{width:40px;height:40px;background:var(--navy);border-radius:4px}
.brand-name{font-family:"Poppins",sans-serif;font-weight:700;font-size:30px;color:var(--navy);letter-spacing:.5px}
.contact-top{top:28px;font-size:16px;color:var(--navy);display:flex;align-items:center;gap:10px;font-weight:500}
.divider-v{width:1px;height:40px;background:var(--line);top:22px}
.social-dot{width:16px;height:16px;border-radius:50%;background:var(--blue);top:35px}
.nav{left:93px;top:87px;width:1107px;height:58px;background:var(--navy);border-radius:29px 0 0 29px;z-index:3}
.nav a{position:absolute;top:20px;color:var(--white);text-decoration:none;font-size:13px;font-weight:500;letter-spacing:.3px}
.nav .active::after{content:"";position:absolute;left:30px;top:28px;width:22px;height:3px;background:var(--white)}

/* hero */
.hero{left:0;top:120px;width:1200px;height:575px}
.hero-text{left:93px;color:var(--white);z-index:2}
.eyebrow{display:flex;align-items:center;gap:12px;font-weight:600;font-size:19px;letter-spacing:.5px}
.eyebrow span{width:38px;height:2px;background:var(--white)}
.hero-title{font-weight:800;font-size:72px;line-height:1;margin-top:22px;letter-spacing:1px}
.hero-title em{font-style:normal;color:var(--blue)}
.hero-tag{font-size:25px;font-weight:400;margin-top:14px}
.btn{display:inline-flex;align-items:center;gap:14px;background:var(--blue);color:var(--white);border-radius:26px;font-weight:600;font-size:13.5px;letter-spacing:.8px;text-decoration:none}
.hero .btn{position:absolute;left:93px;top:332px;height:48px;padding:0 26px;z-index:2}

/* about */
.portrait{left:93px;top:815px;width:355px;height:398px;clip-path:polygon(25% 3%,75% 3%,100% 50%,75% 97%,25% 97%,0 50%);background:linear-gradient(160deg,#c9c2b8,#6f5a48 55%,#3b2c22)}
.hexdot{width:24px;height:27px;clip-path:polygon(50% 0,100% 25%,100% 75%,50% 100%,0 75%,0 25%)}
.person-name{left:93px;top:1243px;width:355px;text-align:center;font-family:"Courier Prime",monospace;font-style:italic;font-size:19px;letter-spacing:3px;color:var(--ink)}
.person-role{left:93px;width:355px;text-align:center;font-size:16px;line-height:24px;color:var(--ink)}
.person-bar{left:253px;top:1322px;width:34px;height:4px;background:var(--blue)}
.about{left:530px;top:770px;width:560px}
.h2{font-weight:700;color:var(--ink);text-transform:uppercase}
.about .h2{font-size:33px;line-height:40px}
.about .lead{font-size:16.5px;line-height:31px;color:var(--ink);font-weight:500;margin-top:20px}
.about p{font-size:15.5px;line-height:31px;margin-top:18px}

/* designations */
.sec-title{left:0;width:1200px;text-align:center}
.tree{left:180px;top:1446px;width:844px;height:20px;border:2px solid var(--navy);border-bottom:none}
.tree-stub{top:1446px;width:2px;height:20px;background:var(--navy)}
.badge{top:1472px;width:130px;height:130px}

.profile{top:1710px;width:310px}
.profile h4{font-size:16px;font-weight:500;color:var(--ink);display:flex;align-items:center;gap:10px;letter-spacing:.4px}
.profile h4 i{width:14px;height:14px;border-radius:50%;border:2.5px solid var(--blue)}
.profile a{display:block;margin-top:24px;font-size:16px;line-height:28px}
.col-line{top:1676px;width:1px;height:176px;background:var(--line)}

/* roles */
.role{top:2018px;width:240px;text-align:center}
.role svg{display:block;margin:0 auto}
.role p{font-size:17px;line-height:27px;color:var(--ink);font-weight:500;margin-top:26px}

/* experience */
.exp-bg{left:0;top:2320px}
.exp-title{top:2570px;color:var(--white);font-size:33px}
.timeline{left:599px;top:2797px;height:1170px;border-left:2px dashed #8ea6cf}
.tnode{width:90px;height:100px}
.block{width:410px;color:var(--white)}
.num{font-size:84px;font-weight:700;line-height:1;display:inline-block;vertical-align:top}
.num small{font-size:84px;color:var(--white)}
.block h3{position:absolute;font-size:17.5px;font-weight:700;text-transform:uppercase;line-height:26px;letter-spacing:.3px}
.ticks{list-style:none}
.ticks li{position:relative;padding-left:35px;font-size:15.5px;line-height:31px;margin-bottom:30px}
.ticks li::before{content:"";position:absolute;left:0;top:7px;width:17px;height:17px;border-radius:50%;background:var(--white)}
.ticks li::after{content:"";position:absolute;left:5px;top:11px;width:6px;height:3.5px;border-left:2px solid var(--navy);border-bottom:2px solid var(--navy);transform:rotate(-45deg)}

/* cta */
.cta{left:0;top:4120px;width:1200px;height:278px;background:linear-gradient(180deg,#eef1f6,#f7f8fb)}
.cta-title{left:93px;top:4208px;border-left:4px solid var(--navy);padding-left:12px;font-size:35px;line-height:42px;color:var(--navy);font-weight:700;text-transform:uppercase}
.cta-btn{left:874px;top:4210px;height:48px;padding:0 28px}

/* footer */
.foot-h{font-size:15px;font-weight:700;color:var(--ink);letter-spacing:.5px}
.foot-links{list-style:none;font-size:15.5px;color:var(--ink)}
.foot-links li{height:36px}
.foot-contact{font-size:15.5px;color:var(--ink);line-height:30px}
.ico{position:absolute;left:-33px;top:7px}
</style>
</head>
<body>

<!-- header -->
<div class="abs brand"><span class="brand-mark"></span><span class="brand-name">Pins &amp; Dials</span></div>
<div class="abs contact-top" style="left:531px">
  <svg width="22" height="16" viewBox="0 0 22 16"><rect x="1" y="1" width="20" height="14" rx="2" fill="none" stroke="#0a8ad6" stroke-width="2"/><path d="M2 2l9 7 9-7" fill="none" stroke="#0a8ad6" stroke-width="2"/></svg>
  hello@pinsanddials.example</div>
<div class="abs divider-v" style="left:778px"></div>
<div class="abs contact-top" style="left:806px">
  <svg width="20" height="20" viewBox="0 0 24 24"><path d="M6 2l4 5-2 3c1 3 3 5 6 6l3-2 5 4-3 4C10 21 3 14 2 5z" fill="none" stroke="#0a8ad6" stroke-width="2"/></svg>
  555-014-2288</div>
<div class="abs divider-v" style="left:985px"></div>
<div class="abs social-dot" style="left:1012px"></div>
<div class="abs social-dot" style="left:1052px"></div>
<div class="abs social-dot" style="left:1092px"></div>

<nav class="abs nav">
  <a href="#" class="active" style="left:40px">WHO AM I</a>
  <a href="#" style="left:175px">PINS &amp; DIALS</a>
  <a href="#" style="left:298px">THE TEAM LEVEL</a>
  <a href="#" style="left:472px">THE PROGRAM LEVEL</a>
  <a href="#" style="left:681px">PRESENTATIONS</a>
  <a href="#" style="left:857px">MONTHLY BLOG</a>
</nav>

<!-- hero -->
<section class="abs hero">
  <svg class="abs" style="left:0;top:0" width="1200" height="575" viewBox="0 0 1200 575">
    <defs>
      <linearGradient id="heroGrad" x1="0" y1="0" x2="1" y2="0.3">
        <stop offset="0" stop-color="#061530"/>
        <stop offset="0.35" stop-color="#0d3a7a"/>
        <stop offset="0.6" stop-color="#0a2350"/>
        <stop offset="1" stop-color="#050f24"/>
      </linearGradient>
    </defs>
    <g role="img" aria-label="Photo of an IT professional working on a laptop in a server room">
      <polygon points="0,0 1200,0 1200,500 0,570" fill="url(#heroGrad)"/>
    </g>
    <polygon points="1200,492 1200,536 520,575 300,575" fill="#0a8ad6"/>
  </svg>
  <div class="abs hero-text" style="top:150px;left:93px">
    <div class="eyebrow"><span></span>WELCOME TO<span></span></div>
    <h1 class="hero-title">PINS <em>&amp;</em> DIALS</h1>
    <p class="hero-tag">Agile IT Coaching &amp; Training.</p>
  </div>
  <a class="btn" href="#">GET IN TOUCH
    <svg width="22" height="14" viewBox="0 0 22 14"><path d="M1 7h19M14 1l6 6-6 6" fill="none" stroke="#fff" stroke-width="2"/></svg></a>
</section>

<!-- about -->
<div class="abs hexdot" style="left:120px;top:822px;background:var(--navy)"></div>
<div class="abs hexdot" style="left:93px;top:848px;background:#cfd4dc;width:30px;height:34px"></div>
<div class="abs portrait" role="img" aria-label="Portrait photo of Brent Holloway"></div>
<div class="abs hexdot" style="left:360px;top:1128px;background:#e3e6eb"></div>
<div class="abs hexdot" style="left:348px;top:1152px;background:var(--blue)"></div>
<div class="abs hexdot" style="left:376px;top:1152px;background:var(--navy)"></div>
<div class="abs person-name">BRENT HOLLOWAY</div>
<div class="abs person-role" style="top:1268px">Senior Scrum Master &amp;<br>Team Agile Coach</div>
<div class="abs person-bar"></div>

<section class="abs about">
  <h2 class="h2">Who am I, what I do,<br>my experience</h2>
  <p class="lead">Demonstrate experience and progression from Scrum Master to Program Manager to Coach</p>
  <p>Brent Holloway is the Owner of Keystride Project Group, LLC and serves as Principal Lead Consultant on waterfall and agile contract opportunities.</p>
  <p style="margin-top:31px">Keystride Project Group, LLC has engaged on a contract basis with Tier One companies across various industries including banking and credit unions, global supply chain, and international food distribution. Brent Holloway brings 12 years of experience to his clients encompassing various project methodologies including: waterfall, agile, and hybrid frameworks.</p>
</section>

<!-- designations -->
<h2 class="abs sec-title h2" style="top:1392px;font-size:21px">Coaching Designations</h2>
<div class="abs tree"></div>
<div class="abs tree-stub" style="left:396px"></div>
<div class="abs tree-stub" style="left:602px"></div>
<div class="abs tree-stub" style="left:806px"></div>

<svg class="abs badge" style="left:115px" viewBox="0 0 130 130" role="img" aria-label="Certification badge"><circle cx="65" cy="65" r="58" fill="#1a8fd0"/><circle cx="65" cy="65" r="46" fill="none" stroke="#fff" stroke-width="3"/></svg>
<svg class="abs badge" style="left:331px" viewBox="0 0 130 130" role="img" aria-label="Educator badge"><circle cx="65" cy="65" r="58" fill="#f39a3c"/><circle cx="65" cy="65" r="46" fill="none" stroke="#fff" stroke-width="3"/></svg>
<svg class="abs badge" style="left:537px" viewBox="0 0 130 130" role="img" aria-label="Certified professional badge"><polygon points="65,6 117,36 117,94 65,124 13,94 13,36" fill="#fff" stroke="#0b2a5e" stroke-width="8"/></svg>
<svg class="abs badge" style="left:741px" viewBox="0 0 130 130" role="img" aria-label="Advanced scrum master badge"><polygon points="65,4 126,65 65,126 4,65" fill="#0b2a5e"/><polygon points="65,22 108,65 65,108 22,65" fill="#1a4c8a"/></svg>
<svg class="abs badge" style="left:955px" viewBox="0 0 130 130" role="img" aria-label="Advanced certification badge"><circle cx="65" cy="65" r="58" fill="#f5b82e"/><circle cx="65" cy="65" r="46" fill="none" stroke="#fff" stroke-width="3"/></svg>

<div class="abs col-line" style="left:389px"></div>
<div class="abs col-line" style="left:735px"></div>
<div class="abs profile" style="left:93px"><h4><i></i>Agile Guild Profile</h4><a href="#">https://www.agileguild.example/<br>community/profile/bholloway10</a></div>
<div class="abs profile" style="left:441px"><h4><i></i>Badgevault Profile</h4><a href="#">https://www.badgevault.example/users/<br>brent-holloway.b71c9d3e</a></div>
<div class="abs profile" style="left:785px;width:340px"><h4><i></i>LYNQ Scaled Alliance Profile</h4><a href="#">https://community.lynq.example/s/<br>profile/0071K0000045bmzRTX</a></div>

<!-- roles -->
<h2 class="abs sec-title h2" style="top:1920px;font-size:32px">Roles I have held</h2>

<div class="abs role" style="left:106px">
  <svg width="120" height="124" viewBox="0 0 120 124"><polygon points="60,10 108,36 108,92 60,118 12,92 12,36" fill="#fff" stroke="#0a8ad6" stroke-width="3"/><polygon points="60,22 97,42 97,86 60,106 23,86 23,42" fill="#0b2a5e"/><circle cx="60" cy="58" r="12" fill="none" stroke="#fff" stroke-width="5"/><rect x="52" y="74" width="16" height="12" fill="#fff"/><circle cx="92" cy="14" r="13" fill="#0a8ad6"/><text x="92" y="19" text-anchor="middle" font-family="Poppins,sans-serif" font-size="14" font-weight="600" fill="#fff">1</text></svg>
  <p>Sr. Scrum<br>Master</p>
</div>
<div class="abs role" style="left:324px">
  <svg width="120" height="124" viewBox="0 0 120 124"><polygon points="60,10 108,36 108,92 60,118 12,92 12,36" fill="#fff" stroke="#0a8ad6" stroke-width="3"/><polygon points="60,22 97,42 97,86 60,106 23,86 23,42" fill="#0b2a5e"/><circle cx="60" cy="56" r="8" fill="#fff"/><circle cx="44" cy="64" r="6" fill="#fff"/><circle cx="76" cy="64" r="6" fill="#fff"/><rect x="48" y="68" width="24" height="14" rx="5" fill="#fff"/><circle cx="92" cy="14" r="13" fill="#0a8ad6"/><text x="92" y="19" text-anchor="middle" font-family="Poppins,sans-serif" font-size="14" font-weight="600" fill="#fff">2</text></svg>
  <p>Advanced LYNQ<br>Scrum Master</p>
</div>
<div class="abs role" style="left:567px">
  <svg width="120" height="124" viewBox="0 0 120 124"><polygon points="60,10 108,36 108,92 60,118 12,92 12,36" fill="#fff" stroke="#0a8ad6" stroke-width="3"/><polygon points="60,22 97,42 97,86 60,106 23,86 23,42" fill="#0b2a5e"/><path d="M46 80l6-18 18-18 6 6-18 18z" fill="#fff"/><circle cx="92" cy="14" r="13" fill="#0a8ad6"/><text x="92" y="19" text-anchor="middle" font-family="Poppins,sans-serif" font-size="14" font-weight="600" fill="#fff">3</text></svg>
  <p>Hybrid Scrum Master<br>Project Manager</p>
</div>
<div class="abs role" style="left:830px">
  <svg width="120" height="124" viewBox="0 0 120 124"><polygon points="60,10 108,36 108,92 60,118 12,92 12,36" fill="#fff" stroke="#0a8ad6" stroke-width="3"/><polygon points="60,22 97,42 97,86 60,106 23,86 23,42" fill="#0b2a5e"/><rect x="44" y="68" width="6" height="14" fill="#fff"/><rect x="54" y="62" width="6" height="20" fill="#fff"/><rect x="64" y="56" width="6" height="26" fill="#fff"/><path d="M44 60l30-16M68 42h7v7" fill="none" stroke="#fff" stroke-width="3"/><circle cx="92" cy="14" r="13" fill="#0a8ad6"/><text x="92" y="19" text-anchor="middle" font-family="Poppins,sans-serif" font-size="14" font-weight="600" fill="#fff">4</text></svg>
  <p style="margin-top:30px">Business (Finance<br>Transformation<br>Program Manager)</p>
</div>

<!-- experience -->
<svg class="abs exp-bg" width="1200" height="1800" viewBox="0 0 1200 1800">
  <defs>
    <linearGradient id="expGrad" x1="0" y1="0" x2="0" y2="1">
      <stop offset="0" stop-color="#0a2350"/>
      <stop offset="0.85" stop-color="#0b2a5e"/>
      <stop offset="1" stop-color="#1b3a6e"/>
    </linearGradient>
  </defs>
  <polygon points="0,10 574,165 0,198" fill="#0a8ad6"/>
  <polygon points="0,198 1200,134 1200,1800 0,1800" fill="url(#expGrad)"/>
</svg>
<h2 class="abs sec-title h2 exp-title">What is my experience</h2>

<div class="abs timeline"></div>
<svg class="abs tnode" style="left:555px;top:2747px" viewBox="0 0 90 100"><polygon points="45,2 88,26 88,74 45,98 2,74 2,26" fill="#fff"/><path d="M32 70V44l13-10 13 10v26M38 70V52h14v18" fill="none" stroke="#0a8ad6" stroke-width="3"/></svg>
<svg class="abs tnode" style="left:555px;top:3061px" viewBox="0 0 90 100"><polygon points="45,2 88,26 88,74 45,98 2,74 2,26" fill="#fff"/><rect x="26" y="34" width="38" height="26" rx="2" fill="none" stroke="#0a8ad6" stroke-width="3"/><path d="M32 54l8-8 6 5 10-10M38 68h14M45 60v8" fill="none" stroke="#0a8ad6" stroke-width="3"/></svg>
<svg class="abs tnode" style="left:555px;top:3432px" viewBox="0 0 90 100"><polygon points="45,2 88,26 88,74 45,98 2,74 2,26" fill="#fff"/><circle cx="42" cy="40" r="8" fill="none" stroke="#0a8ad6" stroke-width="3"/><path d="M28 66c0-10 6-15 14-15s10 3 12 6" fill="none" stroke="#0a8ad6" stroke-width="3"/><circle cx="58" cy="62" r="6" fill="none" stroke="#0a8ad6" stroke-width="3"/></svg>

<div class="abs block" style="left:93px;top:2741px">
  <span class="num">1<small>.</small></span>
  <h3 style="left:80px;top:22px">As a LYNQ Adv Scrum<br>Master, I:</h3>
  <ul class="ticks" style="margin-top:35px">
    <li>Stand up teams</li>
    <li>Run development efforts concurrently leading multiple teams</li>
    <li>Run LYNQ ceremonies</li>
    <li>Scrum of Scrums facilitator</li>
    <li>PI Planning team facilitator (multiple teams on BQR)</li>
    <li>Teach and coach to advanced development team strategies</li>
    <li>Lead program level communications and business status updates on behalf of the</li>
  </ul>
</div>

<div class="abs block" style="left:709px;top:3060px;width:400px">
  <span class="num">2<small>.</small></span>
  <h3 style="left:97px;top:22px">Business Transformation<br>Program Manager</h3>
  <ul class="ticks" style="left:8px;position:relative;margin-top:24px">
    <li>Lead business transformation efforts at the program level</li>
    <li>Work with multiple product owners, business analysts, and business stakeholders on requirements</li>
    <li>Lead the international rollout, onboarding, and support of new transformational CRM tool, CloudLedger</li>
    <li>Standup and lead multi-functional teams consisting of business and technology team members</li>
    <li>Serve as program organization and communications lead</li>
  </ul>
</div>

<div class="abs block" style="left:93px;top:3427px">
  <span class="num">3<small>.</small></span>
  <h3 style="left:80px;top:22px">As a Hybrid Scrum Master /<br>Project Manager, I:</h3>
  <ul class="ticks" style="margin-top:30px">
    <li>Standup teams</li>
    <li>Run multiple program level projects simultaneously</li>
    <li>Implement custom hybrid development strategies</li>
    <li>Manage to project triple constraints</li>
    <li>Communications lead and business liaison</li>
    <li>Use multiple coaching styles based on team and project</li>
  </ul>
</div>

<!-- cta -->
<section class="abs cta"></section>
<h2 class="abs cta-title">Where does coaching<br>come in to play</h2>
<a class="abs btn cta-btn" href="#">GET IN TOUCH
  <svg width="22" height="14" viewBox="0 0 22 14"><path d="M1 7h19M14 1l6 6-6 6" fill="none" stroke="#fff" stroke-width="2"/></svg></a>

<!-- footer -->
<div class="abs brand" style="top:4470px"><span class="brand-mark" style="width:36px;height:36px"></span><span class="brand-name" style="font-size:28px">Pins &amp; Dials</span></div>
<div class="abs" style="left:93px;top:4554px;font-size:15px;font-weight:600;color:var(--ink);letter-spacing:.5px;display:flex;align-items:center;gap:26px">Social Media:
  <span style="width:14px;height:14px;border-radius:50%;background:var(--blue)"></span>
  <span style="width:14px;height:14px;border-radius:50%;background:var(--blue)"></span>
  <span style="width:14px;height:14px;border-radius:50%;background:var(--blue)"></span>
</div>
<div class="abs" style="left:93px;top:4627px;font-size:14.5px;line-height:27px;color:var(--ink)">Copyright © 2022 Pins &amp; Dials.<br>All rights reserved.</div>

<div class="abs" style="left:507px;top:4462px">
  <h4 class="foot-h">SITEMAP</h4>
  <ul class="foot-links" style="margin-top:16px">
    <li>Who am I</li><li>Pins &amp; Dials</li><li>The Team Level</li><li>The Program Level</li><li>Presentations</li><li>Monthly Blog</li>
  </ul>
</div>

<div class="abs" style="left:817px;top:4462px;width:300px">
  <h4 class="foot-h">CONTACT US</h4>
  <div class="foot-contact" style="position:relative;margin:14px 0 0 33px">
    <svg class="ico" width="14" height="18" viewBox="0 0 14 18"><path d="M7 1a6 6 0 0 1 6 6c0 4-6 10-6 10S1 11 1 7a6 6 0 0 1 6-6z" fill="#0a8ad6"/><circle cx="7" cy="7" r="2" fill="#fff"/></svg>
    Consectetur adipiscing elit sed do tempor incididunt ut
  </div>
  <div class="foot-contact" style="position:relative;margin:24px 0 0 33px">
    <svg class="ico" width="16" height="16" viewBox="0 0 24 24"><path d="M6 2l4 5-2 3c1 3 3 5 6 6l3-2 5 4-3 4C10 21 3 14 2 5z" fill="#0a8ad6"/></svg>
    555-014-2288
  </div>
  <div class="foot-contact" style="position:relative;margin:25px 0 0 33px">
    <svg class="ico" width="16" height="13" viewBox="0 0 22 16"><rect x="0" y="0" width="22" height="16" rx="2" fill="#0a8ad6"/><path d="M2 2l9 7 9-7" fill="none" stroke="#fff" stroke-width="2"/></svg>
    hello@pinsanddials.example
  </div>
</div>

</body>
</html>
```